Construction company- stationary project
business card, letterhead, envelopes, presentation folder
Construction company- stationary project -
Creative Brief
Professional
Brent Halloway
38 Percival Ln. Millbrook, NY 12545
brent.halloway@ridgefold-builders.com
www.ridgefold-builders.com
Residential contractor focused on design build, custom, and restoration projects. Emphasizing team concept
open to ideas possibly the logo

```html
<!DOCTYPE html>
<html lang="en">
<head>
<meta charset="utf-8">
<title>Ridgefold Builders – Stationery</title>
<link href="https://fonts.googleapis.com/css2?family=Cinzel:wght@400;600&display=swap" rel="stylesheet">
<style>
  :root {
    --bg: #7a7a7a;
    --blush-light: #fbeee6;
    --blush: #efc9b6;
    --blush-deep: #d9a189;
    --brown: #5b2a22;
    --paper: #ffffff;
    --band: #e6b39d;
  }
  * { margin: 0; padding: 0; box-sizing: border-box; }
  html, body { width: 1200px; height: 991px; overflow: hidden; }
  body {
    position: relative;
    background: var(--bg);
    font-family: "Cinzel", "Times New Roman", serif;
    color: var(--brown);
  }

  .brand { text-align: center; color: var(--brown); line-height: 1; }
  .brand-name { font-size: 26px; font-weight: 400; letter-spacing: 1px; white-space: nowrap; }
  .brand-mark { display: block; width: 14px; height: 14px; background: var(--brown); margin: 0 auto 8px; }

  /* Disc */
  .disc {
    position: absolute; left: 121px; top: 120px; width: 312px; height: 312px;
    border-radius: 50%;
    background: radial-gradient(circle at 50% 45%, var(--blush-light) 0%, var(--blush) 60%, var(--blush-deep) 100%);
    box-shadow: 0 6px 18px rgba(0,0,0,.35);
  }
  .disc-ring {
    position: absolute; left: 50%; top: 50%; width: 118px; height: 118px; transform: translate(-50%,-50%);
    border-radius: 50%; background: var(--paper);
  }
  .disc-hole {
    position: absolute; left: 50%; top: 50%; width: 56px; height: 56px; transform: translate(-50%,-50%);
    border-radius: 50%; background: var(--bg);
  }
  .disc .brand { position: absolute; left: 0; right: 0; top: 222px; }
  .disc .brand-name { font-size: 17px; }
  .disc .brand-mark { width: 10px; height: 10px; margin-bottom: 6px; }

  /* Folder cover */
  .folder-cover {
    position: absolute; left: 537px; top: 27px; width: 631px; height: 435px;
    display: flex; box-shadow: 0 6px 18px rgba(0,0,0,.35);
  }
  .cover-panel {
    position: relative; flex: 1;
    background: radial-gradient(ellipse at 50% 35%, var(--blush-light) 0%, var(--blush) 65%, var(--blush-deep) 100%);
  }
  .cover-back { border-right: 1px solid rgba(91,42,34,.25); }
  .cover-front .brand { position: absolute; left: 0; right: 0; top: 168px; }
  .cover-front .brand-name { font-size: 28px; }
  .cover-contact {
    position: absolute; left: 20px; right: 16px; top: 380px; height: 34px;
    background: var(--brown); color: var(--blush-light);
    font-size: 6px; letter-spacing: 0; padding: 4px 7px; line-height: 1.45;
    white-space: nowrap; overflow: hidden;
  }

  /* Envelope */
  .envelope {
    position: absolute; left: 13px; top: 639px; width: 564px; height: 314px;
    background: var(--paper); box-shadow: 0 6px 18px rgba(0,0,0,.35);
  }
  .envelope .brand { position: absolute; left: 20px; top: 40px; width: 200px; }
  .envelope .brand-name { font-size: 19px; }
  .compliments-band {
    position: absolute; right: 0; top: 40px; width: 255px; height: 41px;
    background: linear-gradient(90deg, var(--blush), var(--band));
    font-size: 22px; padding: 8px 0 0 20px; color: var(--brown);
  }
  .envelope-contact {
    position: absolute; left: 30px; top: 223px; font-size: 8.5px; letter-spacing: .4px; line-height: 1.6;
  }

  /* Folder inside */
  .folder-inside {
    position: absolute; left: 617px; top: 497px; width: 564px; height: 483px;
    background: var(--paper); box-shadow: 0 6px 18px rgba(0,0,0,.35);
  }
  .folder-inside .fold {
    position: absolute; left: 269px; top: 0; bottom: 0; width: 1px; background: rgba(91,42,34,.2);
  }
  .pockets { position: absolute; left: 0; top: 0; }
  .pocket-brand { position: absolute; }
  .pocket-brand .brand-name { font-size: 16px; }
  .pocket-left { left: 40px; top: 420px; width: 150px; }
  .pocket-right { left: 410px; top: 345px; width: 150px; }
</style>
</head>
<body>

  <section class="disc" aria-label="Disc label">
    <div class="disc-ring"></div>
    <div class="disc-hole"></div>
    <div class="brand">
      <span class="brand-mark"></span>
      <span class="brand-name">Ridgefold Builders</span>
    </div>
  </section>

  <section class="folder-cover" aria-label="Presentation folder, outside">
    <div class="cover-panel cover-back">
      <div class="cover-contact">
        38 Percival Ln. Millbrook, NY 12545 &nbsp; Cell: (845) 555-0172<br>
        brent.halloway@ridgefold-builders.com<br>
        www.ridgefold-builders.com
      </div>
    </div>
    <div class="cover-panel cover-front">
      <div class="brand">
        <span class="brand-mark"></span>
        <span class="brand-name">Ridgefold Builders</span>
      </div>
    </div>
  </section>

  <section class="envelope" aria-label="Compliments envelope">
    <div class="brand">
      <span class="brand-mark"></span>
      <span class="brand-name">Ridgefold Builders</span>
    </div>
    <div class="compliments-band">Best Compliments</div>
    <div class="envelope-contact">
      38 Percival Ln. Millbrook, NY 12545<br>
      Cell: (845) 555-0172 &nbsp; brent.halloway@ridgefold-builders.com &nbsp; www.ridgefold-builders.com
    </div>
  </section>

  <section class="folder-inside" aria-label="Presentation folder, inside">
    <svg class="pockets" width="564" height="483" viewBox="0 0 564 483">
      <defs>
        <linearGradient id="pocket-fill" x1="0" y1="0" x2="0" y2="1">
          <stop offset="0" stop-color="#f7dfd2"/>
          <stop offset="1" stop-color="#e2ad96"/>
        </linearGradient>
      </defs>
      <path d="M0 300 L150 300 C220 300 250 380 268 483 L0 483 Z" fill="url(#pocket-fill)"/>
      <path d="M270 483 C285 360 320 250 420 250 L564 250 L564 483 Z" fill="url(#pocket-fill)"/>
    </svg>
    <div class="fold"></div>
    <div class="brand pocket-brand pocket-left">
      <span class="brand-mark"></span>
      <span class="brand-name">Ridgefold</span>
    </div>
    <div class="brand pocket-brand pocket-right">
      <span class="brand-mark"></span>
      <span class="brand-name">Ridgefold</span>
    </div>
  </section>

</body>
</html>
```